Design a Website Mockup for Plumbing Company

We need to redesign this site: [url removed, login to view]

We need a full-width layout

Same logo and navigation (change Photos to Gallery)

Add social to header and footer

Colors: Light blue (like logo)/ Black / White or Gray

Client would like a clean, professional design

We need to add a place for their licensing number in the footer

They like the main image text on their current site ("You work too hard for your money just to watch it go down the drain...") and would like to use it on the homepage of their new site, but they DO NOT like the main image used on the current site

Homepage mockup only (psd)

```html
<!DOCTYPE html>
<html lang="en">
<head>
<meta charset="utf-8">
<title>Hale's Plumbing – Home</title>
<link href="https://fonts.googleapis.com/css2?family=Lato:wght@300;400;700&family=Open+Sans:ital,wght@0,400;0,600;0,700;1,400&display=swap" rel="stylesheet">
<style>
:root{
  --blue:#2a86dc;
  --blue-dark:#1f6fbf;
  --ink:#333;
  --text:#555;
  --muted:#888;
  --light:#f2f2f2;
  --topbar:#f5f5f5;
  --footer:#454545;
  --dark-btn:#3c3c3c;
  --white:#fff;
}
*{box-sizing:border-box;margin:0;padding:0}
html,body{width:1200px;height:2892px;overflow:hidden}
body{position:relative;font-family:"Open Sans",Arial,sans-serif;color:var(--text);background:var(--white)}
.abs{position:absolute}
h1,h2,h3{font-family:"Lato",Arial,sans-serif;font-weight:400;color:var(--ink)}
.accent{color:var(--blue)}
.btn{position:absolute;display:flex;align-items:center;justify-content:center;font-family:"Open Sans",Arial,sans-serif;font-size:12px;text-transform:uppercase;background:var(--blue);color:var(--white)}

/* top bar */
.topbar{left:0;top:0;width:1200px;height:40px;background:var(--topbar);font-size:12px;color:#555}
.topbar .info{left:130px;top:12px;display:flex;gap:12px;align-items:center}
.topbar .sep{width:1px;height:16px;background:#ccc}
.topbar .social{right:130px;top:13px;display:flex;gap:12px}
.dot{width:12px;height:12px;border-radius:50%;background:var(--blue)}

/* nav */
.nav{left:0;top:40px;width:1200px;height:70px;background:var(--white)}
.logo{left:130px;top:12px;display:flex;align-items:center;gap:8px;font-family:"Lato",sans-serif;font-weight:700;font-size:18px;color:var(--blue);line-height:1.1}
.logo .mark{width:22px;height:22px;border-radius:50%;background:var(--blue)}
.menu{left:493px;top:25px;display:flex;gap:20px;font-size:14px;color:#444}
.menu .active{color:var(--blue)}

/* hero */
.hero{left:0;top:110px;width:1200px;height:502px;background:linear-gradient(100deg,#8a9fb2 0%,#b7c3ce 30%,#d8d9dc 55%,#e3e3e5 100%)}
.hero h1{position:absolute;left:575px;top:178px;width:520px;font-size:28px;line-height:34px;color:#444}

/* welcome */
.welcome h2{left:130px;top:666px;font-size:31px}
.rule{height:2px;background:var(--blue)}
.welcome p{position:absolute;left:128px;width:625px;font-size:13px;line-height:17px;color:#555}
.welcome-img{left:770px;top:670px;width:430px;height:275px;background:radial-gradient(ellipse at 60% 60%,#c9ccd0 0%,#e8eaec 55%,#fff 75%)}

/* services */
.services{left:0;top:988px;width:1200px;height:412px;background:var(--light)}
.section-title{position:absolute;left:0;width:1200px;text-align:center;font-size:29px}
.title-line{position:absolute;height:2px;background:var(--blue);width:80px}
.service{position:absolute;top:104px;width:300px;text-align:center}
.service .icon{width:100px;height:100px;border-radius:50%;background:var(--white);margin:0 auto;display:flex;align-items:center;justify-content:center}
.service .icon.on{background:var(--blue)}
.service h3{font-family:"Open Sans",sans-serif;font-size:16px;margin-top:22px;color:#333}
.service h3.accent{color:var(--blue)}
.service p{font-size:13px;line-height:17px;margin-top:20px;color:#555}

/* call band */
.band{left:0;top:1400px;width:1200px;height:284px;background:var(--blue)}
.band h2{position:absolute;left:130px;top:66px;font-size:29px;color:var(--white)}
.band .sub{position:absolute;left:131px;top:119px;font-size:13px;color:var(--white)}
.band .btn{left:130px;top:165px;width:160px;height:30px;background:var(--white);color:var(--blue);font-size:11px}
.band-img{left:815px;top:0;width:385px;height:284px;background:linear-gradient(90deg,#cfcbc4,#8c7a66 45%,#3b3330)}

/* testimonial */
.testi{left:0;top:1684px;width:1200px;height:364px;background:var(--light)}
.avatar{left:558px;top:1769px;width:74px;height:74px;border-radius:50%;background:#9aa3ad;border:2px solid #fff}
.quote{left:290px;top:1866px;width:620px;text-align:center;font-size:13px;line-height:17px;color:#666}
.name{left:0;top:1937px;width:1200px;text-align:center;font-size:17px;color:#333}
.place{left:0;top:1963px;width:1200px;text-align:center;font-size:11px;color:var(--blue)}
.dots{left:572px;top:2008px;display:flex;gap:6px}
.dots span{width:8px;height:8px;border-radius:50%;border:1px solid #777}
.dots span.on{background:#555}

/* news */
.card{position:absolute;top:2150px;width:300px}
.card .photo{width:300px;height:187px;position:relative}
.card .date{position:absolute;left:0;top:0;width:48px;text-align:center;color:#fff;font-family:"Lato",sans-serif}
.card .date .d{background:var(--blue);height:40px;font-size:24px;line-height:40px}
.card .date .m{background:#555;height:30px;font-size:16px;line-height:30px}
.card .meta{font-size:13px;font-style:italic;color:#666;margin-top:11px}
.card .meta em{color:var(--blue)}
.card h3{font-family:"Open Sans",sans-serif;font-size:15px;line-height:17px;margin-top:7px;text-transform:uppercase;color:#333}
.card h3.on{color:var(--blue)}
.card p{font-size:13px;line-height:18px;margin-top:19px;color:#666}
.card .btn{position:relative;width:160px;height:36px;margin-top:21px;font-size:14px;background:var(--dark-btn)}
.card .btn.on{background:var(--blue)}

/* footer */
.footer{left:0;top:2648px;width:1200px;height:244px;background:var(--footer);color:#fff}
.footer h4{position:absolute;top:42px;font-size:13px;font-weight:600;text-transform:uppercase}
.footer .frule{position:absolute;top:66px;width:30px;height:2px;background:var(--blue)}
.footer ul{position:absolute;top:92px;list-style:none;font-size:11px;line-height:24px}
.footer .ico{display:inline-block;width:8px;height:8px;border-radius:50%;background:var(--blue);margin-right:8px}
.fsocial{left:752px;top:95px;display:flex;gap:11px}
.fsocial span{width:26px;height:26px;border-radius:50%;background:#fff}
.subscribe{left:752px;top:134px;font-size:13px;line-height:18px;font-weight:600;text-transform:uppercase}
.form{left:752px;top:2815px;width:303px;height:35px;border:1px solid #ddd;display:flex;align-items:center;font-size:10px;color:#fff}
.form .field{flex:1;padding-left:18px}
.form .go{width:90px;text-align:center;border-left:1px solid #777;line-height:33px}
</style>
</head>
<body>

<header>
  <div class="abs topbar">
    <div class="abs info">
      <span>PO Box 41530, Amarillo, Texas 79114</span>
      <span class="sep"></span>
      <span>806-555-0142</span>
    </div>
    <div class="abs social" aria-label="Social links"><span class="dot"></span><span class="dot"></span><span class="dot"></span></div>
  </div>
  <nav class="abs nav">
    <div class="abs logo"><span class="mark"></span><span>Hale's<br>Plumbing</span></div>
    <div class="abs menu">
      <span class="active">Home</span><span>About</span><span>Services</span><span>Gallery</span><span>Blog</span><span>Contact</span>
    </div>
    <span class="btn" style="left:909px;top:20px;width:161px;height:30px;font-size:12px">Request Service Call</span>
  </nav>
</header>

<section class="abs hero" role="img" aria-label="Photo of blue-grey metal plumbing pipes and valves on a textured wall">
  <h1>You Work Too Hard For Your Money Just To Watch It Go Down The Drain...</h1>
  <span class="btn" style="left:576px;top:275px;width:113px;height:30px;font-size:11px">Contact Us</span>
</section>

<section class="welcome">
  <h2 class="abs">Welcome to <span class="accent">Hale's</span> Plumbing</h2>
  <div class="abs rule" style="left:130px;top:728px;width:82px"></div>
  <p style="top:761px">Are you in need of a plumber in Amarillo, Texas? Did your water heater go out or do you need a gas or waterline installed in your home? No matter what's happened to your home or business plumbing, Hale's Plumbing can handle your needs.</p>
  <p style="top:827px">Not only can we handle any plumbing problem you throw our way, we do quickly and professionally. We make it our goal to make sure that you get the absolute best possible service and for a great price.</p>
  <span class="btn" style="left:130px;top:909px;width:113px;height:30px;font-size:11px">Read More</span>
  <div class="abs welcome-img" role="img" aria-label="Photo of braided steel water hoses and brass fittings"></div>
</section>

<section class="abs services">
  <div class="title-line" style="left:350px;top:44px"></div>
  <h2 class="section-title" style="top:26px"><span class="accent">How</span> can we help you?</h2>
  <div class="title-line" style="left:770px;top:44px"></div>

  <div class="service" style="left:127px">
    <div class="icon on"><svg width="50" height="50" viewBox="0 0 50 50" fill="none" stroke="#fff" stroke-width="2"><rect x="20" y="6" width="10" height="38" rx="2"/><rect x="14" y="4" width="22" height="6"/><rect x="14" y="40" width="22" height="6"/><rect x="30" y="19" width="12" height="12"/><line x1="42" y1="16" x2="42" y2="34"/></svg></div>
    <h3 class="accent">Faucet repair and installation.</h3>
    <p>We are new piping experts. We lay pipe professionally and quickly. Don't go to someone who is going to do second class work and charge you an arm and a leg. Contact Hale's Plumbing today!</p>
  </div>
  <div class="service" style="left:450px">
    <div class="icon"><svg width="60" height="50" viewBox="0 0 60 50" fill="none" stroke="#333" stroke-width="2"><circle cx="30" cy="14" r="10"/><line x1="30" y1="14" x2="35" y2="9"/><rect x="26" y="24" width="8" height="6"/><rect x="4" y="30" width="52" height="12"/><line x1="20" y1="30" x2="20" y2="42"/><line x1="40" y1="30" x2="40" y2="42"/></svg></div>
    <h3>Gas line repair and installation.</h3>
    <p>Don't trust your gas plumbing to just anyone. Work that is done properly is crucial when it comes to gas lines in your home and business. Hale's Plumbing is the absolute best when it comes to gas lines and plumbing.</p>
  </div>
  <div class="service" style="left:770px">
    <div class="icon"><svg width="50" height="56" viewBox="0 0 50 56" fill="none" stroke="#333" stroke-width="2"><rect x="12" y="4" width="26" height="40" rx="3"/><line x1="20" y1="12" x2="30" y2="12"/><circle cx="25" cy="34" r="3"/><path d="M18 44 Q18 52 8 52 M32 44 Q32 52 42 52"/></svg></div>
    <h3>Water heater repair and installation</h3>
    <p>Busted water heaters are the worst! Flooded floors and no hot water makes life more than just a little difficult. Let Hale's Plumbing set you up with a new hot water heater professionally and for a great price.</p>
  </div>
</section>

<section class="abs band">
  <h2>Are you in need of a plumber in Amarillo, Texas?</h2>
  <p class="sub">GET THE FAST, AFFORDABLE, AND EXPERT SERVICE THAT YOU DESERVE.</p>
  <span class="btn">Request Service Call</span>
  <div class="abs band-img" role="img" aria-label="Photo of a plumber servicing a hot water heater"></div>
</section>

<section class="abs testi">
  <div class="title-line" style="left:350px;top:44px"></div>
  <h2 class="section-title" style="top:26px">What our <span class="accent">clients</span> say</h2>
  <div class="title-line" style="left:770px;top:44px"></div>
</section>
<div class="abs avatar" role="img" aria-label="Client portrait"></div>
<p class="abs quote">Lorem ipsum dolor sit amet, consectetur adipisicing elit, sed do eiusmod tempor incididunt ut labore et dolore magna aliqua. Ut enim ad minim veniam, quis nostrud exercitation ullamco laboris nisi ut aliquip ex ea commodo consequat.</p>
<p class="abs name">Mark Delaney</p>
<p class="abs place">(Amarila area 123 Lorem Ipsum)</p>
<div class="abs dots"><span></span><span class="on"></span><span></span><span></span></div>

<section class="news">
  <div class="title-line" style="left:410px;top:2098px"></div>
  <h2 class="section-title" style="top:2080px">Latest <span class="accent">News</span></h2>
  <div class="title-line" style="left:710px;top:2098px"></div>

  <article class="card" style="left:130px">
    <div class="photo" role="img" aria-label="Photo of a white pipe laid in a dirt trench" style="background:linear-gradient(160deg,#c79a6a,#9b6b40 60%,#7a5030)">
      <div class="date"><div class="d">14</div><div class="m">June</div></div>
    </div>
    <p class="meta">By <em>Admin</em>, 14 comments</p>
    <h3 class="on">Lorem ipsum dolor sit amet consectetur adipisicing</h3>
    <p>Lorem ipsum dolor sit amet, consectetur adipisicing elit, sed do eiusmod tempor incididunt ut labore et dolore magna aliqua. Ut enim ad minim veniam, quis nostrud exercitation ullamco</p>
    <span class="btn on">Learn More</span>
  </article>
  <article class="card" style="left:450px">
    <div class="photo" role="img" aria-label="Photo of PVC pipe fittings in excavated soil" style="background:linear-gradient(160deg,#8f7a5a,#6d5238 60%,#a89c8a)">
      <div class="date"><div class="d">14</div><div class="m">June</div></div>
    </div>
    <p class="meta">By <em style="color:#666">Admin</em>, 14 comments</p>
    <h3>Lorem ipsum dolor sit amet consectetur adipisicing</h3>
    <p>Lorem ipsum dolor sit amet, consectetur adipisicing elit, sed do eiusmod tempor incididunt ut labore et dolore magna aliqua. Ut enim ad minim veniam, quis nostrud exercitation ullamco</p>
    <span class="btn">Learn More</span>
  </article>
  <article class="card" style="left:770px">
    <div class="photo" role="img" aria-label="Photo of chrome pipes with blue valve handles" style="background:linear-gradient(160deg,#e4e6e8,#b9c0c7 55%,#8fa3b8)">
      <div class="date"><div class="d">14</div><div class="m">June</div></div>
    </div>
    <p class="meta">By <em style="color:#666">Admin</em>, 14 comments</p>
    <h3>Lorem ipsum dolor sit amet consectetur adipisicing</h3>
    <p>Lorem ipsum dolor sit amet, consectetur adipisicing elit, sed do eiusmod tempor incididunt ut labore et dolore magna aliqua. Ut enim ad minim veniam, quis nostrud exercitation ullamco</p>
    <span class="btn">Learn More</span>
  </article>
</section>

<footer class="abs footer">
  <h4 style="left:130px">Our Licence</h4><div class="frule" style="left:130px"></div>
  <ul style="left:130px"><li>#58210</li></ul>

  <h4 style="left:318px">Quick Links</h4><div class="frule" style="left:318px"></div>
  <ul style="left:318px"><li>Home</li><li>Services</li><li>Gallery</li><li>Contact Us</li></ul>

  <h4 style="left:508px">Contact Us</h4><div class="frule" style="left:508px"></div>
  <ul style="left:498px">
    <li><span class="ico"></span>806-555-0142</li>
    <li><span class="ico"></span>hello@halesplumbing.example</li>
    <li><span class="ico"></span>PO Box 41530, Amarillo,</li>
    <li style="padding-left:16px">Texas 79114</li>
  </ul>

  <h4 style="left:752px">Stay Connected</h4><div class="frule" style="left:752px"></div>
  <div class="abs fsocial" aria-label="Social links"><span></span><span></span><span></span><span></span><span></span></div>
  <p class="abs subscribe">Subscribe in our news letter</p>
</footer>
<div class="abs form"><span class="field">Enter Your Email Address</span><span class="go">SUBSCRIBE</span></div>

</body>
</html>
```